Wellness bold & beautiful PowerPoint Template

I will like a PowerPoint template, matching my brand, designed for my business.
- Some words that describe our brand identity are: wellness, natural, calming, simplicity, clean
- For icons, we prefer line icons.
- Website: http://www.verinaxo.com/
- PowerPoint board: https://www.pinboardly.com/tesmaruli/verinaxo-powerpoint/
- Branding board: https://www.pinboardly.com/tesmaruli/verinaxo-branding/
FYI: I am attaching a rough draft of a powerpoint presentation we are preparing
Target Market(s)
Women 23-48 interested in wellness
Industry/Entity Type
Health And Wellness
Font styles to use
Other font styles liked:
- Open Sans, Helvitica, Meddon
Requirements
Must have
- cover page, about page, author page, table of content, table format, graph format, list format, 2 column template.
Nice to have
- time line page sample

```html
<!DOCTYPE html>
<html lang="en">
<head>
<meta charset="utf-8">
<title>Verinaxo – Unclutter Your Space template</title>
<link rel="stylesheet" href="https://fonts.googleapis.com/css2?family=Meddon&family=Open+Sans:wght@400;600;700&display=swap">
<style>
:root{
  --lime:#a5c857;
  --green:#6a9f45;
  --deep-green:#4f8a35;
  --magenta:#a4167e;
  --ink:#3f3f3f;
  --muted:#666;
  --white:#fff;
  --frame:#c9c9c9;
}
*{box-sizing:border-box;margin:0;padding:0}
html,body{width:1058px;height:1200px;overflow:hidden;background:var(--frame)}
body{font-family:"Open Sans",Helvetica,Arial,sans-serif;color:var(--ink)}
.deck{display:grid;grid-template-columns:528px 528px;grid-template-rows:repeat(4,298px);gap:2px;width:1058px;height:1200px}
.slide{position:relative;overflow:hidden;background:var(--white)}
.abs{position:absolute}
.script{font-family:"Meddon",cursive;color:var(--magenta);font-weight:400;line-height:1.2}
.page-dot{position:absolute;right:14px;bottom:6px;width:9px;height:9px;border-radius:50%;background:var(--magenta)}
ul.bullets{list-style:none}
ul.bullets li{position:relative;padding-left:13px}
ul.bullets li::before{content:"•";position:absolute;left:0}
ul.bullets li.sub{padding-left:32px}
ul.bullets li.sub::before{content:"–";left:20px}

/* cover */
.cover-photo{left:0;top:0;width:528px;height:208px;background:linear-gradient(180deg,#4f86c9 0%,#9cc0e6 55%,#c9dcee 72%,#5f8e3a 80%,#3d6d2a 100%)}
.cover-band{left:0;top:208px;width:528px;height:62px;background:var(--lime)}
.cover-brand{left:20px;top:226px;font-size:20px;font-weight:600;color:var(--magenta)}
.cover-tag{left:18px;top:256px;font-size:5.5px;color:#6b7f3e;letter-spacing:.3px}
.cover-title{left:174px;top:220px;font-size:29px;font-weight:600;color:var(--magenta)}
.cover-strip{left:0;top:270px;width:528px;height:22px;background:var(--green);border-bottom:3px solid var(--magenta)}
.cover-credits{right:22px;top:274px;font-size:8.5px;color:var(--white);display:flex;gap:14px}
.cover-credits span::before{content:"•";color:var(--magenta);margin-right:8px}

/* about */
.about-photo{left:15px;top:15px;width:500px;height:224px;background:linear-gradient(160deg,#9ed0c2 0%,#3f9c8a 40%,#1f6f66 70%,#5a7a74 100%)}
.about-box{left:0;top:105px;width:236px;height:90px;background:var(--green);padding:8px 0 0 26px;font-size:29px}
.about-rule{left:15px;top:244px;width:500px;height:2px;background:var(--magenta)}
.about-head{left:18px;top:252px;font-size:15px;font-weight:600;color:#444}
.about-sub{left:18px;top:270px;font-size:9px;color:var(--muted)}

/* list */
.list-bg{left:14px;top:14px;width:500px;height:268px;background:radial-gradient(circle at 85% 30%,#dbe9b5 0%,#eef4d9 45%,#f7f9ee 100%)}
.list-title{left:0;top:18px;width:236px;height:36px;background:var(--green);padding:4px 0 0 20px;font-size:19px}
.list-body{left:32px;top:72px;width:470px;font-size:9.5px;line-height:1.25;color:#444}
.list-body li{margin-bottom:10px}

/* author */
.forest{left:0;top:0;width:528px;height:298px;background:linear-gradient(180deg,#dfeec7 0%,#9cc66a 35%,#5c8f3a 70%,#3c6127 100%)}
.portrait{left:193px;top:32px;width:140px;height:140px;border-radius:50%;border:3px solid #d9d9d9;background:radial-gradient(circle,#a88064 0%,#6e4f3e 60%,#9b8a7c 100%)}
.author-name{left:0;top:170px;width:528px;text-align:center;font-size:20px}
.author-tag{left:0;top:203px;width:528px;text-align:center;font-size:8px;font-weight:700;color:var(--magenta)}
.author-rule{left:194px;top:218px;width:140px;height:1px;background:var(--magenta)}
.author-card{left:68px;top:230px;width:392px;height:48px;background:var(--white);border-radius:8px;display:grid;grid-template-columns:1fr 1fr;padding:10px 14px;font-size:9.5px;line-height:1.3;color:#444}

/* agenda */
.agenda-photo{left:0;top:0;width:528px;height:117px;background:linear-gradient(100deg,#f6eef6 0%,#e4efcf 30%,#8ec24e 60%,#4d8a2d 100%)}
.agenda-title{left:20px;top:40px;font-size:25px}
.agenda-rule{left:0;top:117px;width:528px;height:2px;background:var(--magenta)}
.agenda-col{top:128px;font-size:9.5px;line-height:1.52;color:#444}

/* question */
.hair-photo{left:0;top:0;width:528px;height:298px;background:linear-gradient(100deg,#3b2a22 0%,#6a4a3a 22%,#b9a3a6 45%,#d8cfd6 70%,#c9c0cc 100%)}
.question-band{left:158px;top:30px;width:370px;height:54px;background:var(--green);padding:14px 0 0 14px;font-size:18px;white-space:nowrap}

/* table */
.table-panel{left:0;top:0;width:152px;height:298px;background:var(--green);padding:58px 12px 0 20px;color:var(--white);font-size:9.5px;line-height:1.25}
.table-panel .script{color:var(--white);font-size:17px;margin-bottom:12px}
.table-panel p{margin-bottom:12px}
.table-strip{left:152px;top:0;width:73px;height:298px;background:linear-gradient(90deg,#2f5a22,#8fbf55 50%,#3d6b2a)}
.table-box{left:237px;top:35px;width:280px;height:248px;border:2px solid #666;padding:14px 4px 0 4px}
.data{width:100%;border-collapse:collapse;font-size:7px;color:#666}
.data th{text-align:left;font-weight:600;color:#444;padding:1px 3px;border-bottom:1px solid #999;height:11px}
.data td{padding:0 3px;height:11.4px;border-bottom:1px solid #d4d4d4}
.data tr:nth-child(even) td{background:#f1f1f1}

/* two column */
.twocol-bg{left:0;top:0;width:528px;height:298px;background:linear-gradient(110deg,#6fa24a 0%,#5e9240 45%,#3f6b2a 75%,#2d4f1e 100%)}
.twocol-title{left:40px;top:40px;font-size:26px;color:var(--white)}
.twocol-text{top:88px;width:202px;font-size:9.3px;line-height:1.18;color:var(--white)}
.twocol-text p{margin-bottom:10px}
</style>
</head>
<body>
<main class="deck">

  <section class="slide cover">
    <div class="abs cover-photo" role="img" aria-label="Photo: woman on a bicycle in a flowering meadow under a blue sky"></div>
    <div class="abs cover-band"></div>
    <div class="abs cover-brand">Verinaxo</div>
    <div class="abs cover-tag">SUPPORTING YOUR WELLNESS JOURNEY</div>
    <h1 class="abs cover-title">Unclutter Your Space</h1>
    <div class="abs cover-strip"></div>
    <div class="abs cover-credits"><span>Tesa Maruli @ Verinaxo</span><span>Dalia Fenwick @ Simply Dalia</span></div>
  </section>

  <section class="slide about">
    <div class="abs about-photo" role="img" aria-label="Photo: hand touching clear turquoise water"></div>
    <h2 class="abs about-box script">About<br>Verinaxo</h2>
    <div class="abs about-rule"></div>
    <div class="abs about-head">Supporting Your Wellness Journey:</div>
    <div class="abs about-sub">Helping people live healthier (happier), more balanced and holistic lives</div>
  </section>

  <section class="slide list">
    <div class="abs list-bg" role="img" aria-label="Soft faded photo of green leaves"></div>
    <h2 class="abs list-title script">List Slide</h2>
    <ul class="abs bullets list-body">
      <li>Lorem ipsum dolor sit amet, consectetuer adipiscing elit. Maecenas porttitor congue massa. Fusce posuere, magna sed pulvinar ultricies, purus lectus malesuada libero, sit amet commodo magna eros quis urna.</li>
      <li>Nunc viverra imperdiet enim. Fusce est. Vivamus a tellus.</li>
      <li>Pellentesque habitant morbi tristique senectus et netus et malesuada fames ac turpis egestas. Proin pharetra nonummy pede. Mauris et orci. Lorem ipsum dolor sit amet, consectetuer adipiscing elit.</li>
      <li>Maecenas porttitor congue massa. Fusce posuere, magna sed pulvinar ultricies, purus lectus malesuada libero, sit amet commodo magna eros quis urna.</li>
      <li>Pellentesque habitant morbi tristique senectus et netus et malesuada fames ac turpis egestas. Proin pharetra nonummy pede. Mauris et orci.</li>
    </ul>
    <span class="page-dot"></span>
  </section>

  <section class="slide author">
    <div class="abs forest" role="img" aria-label="Photo: looking up into a sunlit green forest canopy"></div>
    <div class="abs portrait" role="img" aria-label="Circular portrait photo of the author with her son"></div>
    <h2 class="abs author-name script">Tesa</h2>
    <div class="abs author-tag">Creating a happier more balanced life for me and my family</div>
    <div class="abs author-rule"></div>
    <div class="abs author-card">
      <ul class="bullets"><li>Software Engineer by Training</li><li>Mom of 2 boys</li></ul>
      <ul class="bullets"><li>Since 2010, developing a holistic lifestyle</li><li>Knack for organization and efficiency</li></ul>
    </div>
  </section>

  <section class="slide agenda">
    <div class="abs agenda-photo" role="img" aria-label="Photo: sunlit green leaves on a branch"></div>
    <h2 class="abs agenda-title script">Agenda</h2>
    <div class="abs agenda-rule"></div>
    <ul class="abs bullets agenda-col" style="left:32px">
      <li>Why Unclutter</li><li>The Point of Frustration</li><li>Failed Attempts</li><li>Getting Help</li>
      <li>Steps to creating your best space</li>
      <li class="sub">Declutter</li><li class="sub">Organize</li><li class="sub">Rejuvenate</li><li class="sub">Maintain</li>
      <li>Before &amp; After</li><li>Keeping it real!</li>
    </ul>
    <ul class="abs bullets agenda-col" style="left:275px">
      <li>Getting Started</li><li>Declutter Action Plan</li><li>Organizational principles – Tips &amp; Tricks</li>
      <li>Feng Shui101</li><li>It’s not just the clutter</li><li>Zero Waste Movement</li><li>Getting stuck</li>
      <li class="sub">Circleboard Forum</li><li class="sub">Professional help</li><li>Resources</li>
    </ul>
    <span class="page-dot"></span>
  </section>

  <section class="slide question">
    <div class="abs hair-photo" role="img" aria-label="Photo: woman with long hair seen from behind against a misty sky"></div>
    <h2 class="abs question-band script">What Brings You Here Today?</h2>
  </section>

  <section class="slide table-slide">
    <div class="abs table-panel">
      <h2 class="script">Table/Chart</h2>
      <p>Describe the table here:</p>
      <p>Lorem ipsum dolor sit amet, consectetuer adipiscing elit. Maecenas porttitor congue massa. Fusce posuere, magna sed pulvinar ultricies, purus lectus malesuada libero, sit amet commodo magna eros quis urna.</p>
    </div>
    <div class="abs table-strip" role="img" aria-label="Photo strip: tall forest trees"></div>
    <div class="abs table-box">
      <table class="data">
        <thead><tr><th>Date</th><th>Series 1</th><th>Series 2</th><th>Series 3</th></tr></thead>
        <tbody>
          <tr><td>27/11</td><td>0</td><td>0</td><td>3200</td></tr>
          <tr><td>24/10</td><td>0</td><td>0</td><td>2300</td></tr>
          <tr><td>17/10</td><td>0</td><td>0</td><td>0</td></tr>
          <tr><td>15/12</td><td>0</td><td>0</td><td>0</td></tr>
          <tr><td>15/11</td><td>0</td><td>0</td><td>2000</td></tr>
          <tr><td>15/1</td><td>0</td><td>0</td><td>3400</td></tr>
          <tr><td>13/12</td><td>0</td><td>0</td><td>0</td></tr>
          <tr><td>12/12</td><td>0</td><td>0</td><td>0</td></tr>
          <tr><td>10/12</td><td>0</td><td>0</td><td>0</td></tr>
          <tr><td>09/1</td><td>0</td><td>0</td><td>0</td></tr>
          <tr><td>07/11</td><td>0</td><td>0</td><td>0</td></tr>
          <tr><td>04/12</td><td>0</td><td>0</td><td>0</td></tr>
          <tr><td>04/11</td><td>66</td><td>0</td><td>0</td></tr>
          <tr><td>03/11</td><td>75</td><td>0</td><td>0</td></tr>
          <tr><td>02/11</td><td>200</td><td>0</td><td>0</td></tr>
          <tr><td>02/10</td><td>0</td><td>0</td><td>0</td></tr>
          <tr><td>01/12</td><td>0</td><td>0</td><td>0</td></tr>
          <tr><td>01/11</td><td>450</td><td>0</td><td>0</td></tr>
          <tr><td>01/1</td><td>0</td><td>0</td><td>0</td></tr>
        </tbody>
      </table>
    </div>
    <span class="page-dot"></span>
  </section>

  <section class="slide two-column">
    <div class="abs twocol-bg" role="img" aria-label="Photo: green forest with a wooden bench, tinted green"></div>
    <h2 class="abs twocol-title script">Two Column Slide</h2>
    <div class="abs twocol-text" style="left:44px">
      <p>Lorem ipsum dolor sit amet, consectetuer adipiscing elit. Maecenas porttitor congue massa. Fusce posuere, magna sed pulvinar ultricies, purus lectus malesuada libero, sit amet commodo magna eros quis urna.</p>
      <p>Nunc viverra imperdiet enim. Fusce est. Vivamus a tellus.</p>
      <p>Pellentesque habitant morbi tristique senectus et netus et malesuada fames ac turpis egestas. Proin pharetra nonummy pede. Mauris et orci. Lorem ipsum dolor sit amet, consectetuer adipiscing elit. Maecenas porttitor congue massa. Fusce posuere, magna sed pulvinar ultricies, purus lectus malesuada libero, sit amet commodo magna eros quis urna.</p>
    </div>
    <div class="abs twocol-text" style="left:272px">
      <p>Pellentesque habitant morbi tristique senectus et netus et malesuada fames ac turpis egestas. Proin pharetra nonummy pede. Mauris et orci.<br>Lorem ipsum dolor sit amet, consectetuer adipiscing elit. Maecenas porttitor congue massa. Fusce posuere, magna sed pulvinar ultricies, purus lectus malesuada libero, sit amet commodo magna eros quis urna.</p>
      <p>Nunc viverra imperdiet enim. Fusce est. Vivamus a tellus.</p>
      <p>Pellentesque habitant morbi tristique senectus et netus et malesuada fames ac turpis egestas. Proin pharetra nonummy pede. Mauris et orci.</p>
    </div>
  </section>

</main>
</body>
</html>
```